Business Cards- The Manor at Brookridge Golf Club

We would like our business cards to look more high-end. We are a wedding venue that has been in business for 60+ years. We like our logo and our colors - primarily green and a touch of gold/beige. The owner wants our business cards to look more special..

Target Market(s)

Brides who have already toured our venue

Industry/Entity Type

Wedding venue - mansion

Contact Information for Business Card

Name, email, physical address, phone number

Colors
00AB8E
00BBA5
67D7C9
C6EFE9
E9F9F6

Requirements
Must have
• I think we would like our cards to be so pretty that people will want to keep them and will remember the venue. The venue is historic (built in 1850) and beautiful.
Nice to have
• Could we put an image of the building on one side and the contact info on the other?
Should not have
• The color black

```html
<!DOCTYPE html>
<html lang="en">
<head>
<meta charset="utf-8">
<title>The Manor at Brookridge Golf Club – Business Cards</title>
<link href="https://fonts.googleapis.com/css2?family=Montserrat:wght@400;500;700&display=swap" rel="stylesheet">
<style>
  :root {
    --stage: #e6e8e1;
    --card-green: #88a03e;
    --brand-green: #6f8f24;
    --brand-green-deep: #5f7c1e;
    --paper: #fdfdfb;
    --gold: #cdbb98;
    --ink-soft: #4b4b46;
  }
  * { box-sizing: border-box; margin: 0; padding: 0; }
  html, body {
    width: 1200px; height: 1186px; overflow: hidden;
    background: var(--stage);
    font-family: "Montserrat", sans-serif;
  }
  .stage {
    position: relative; width: 1200px; height: 1186px;
    display: flex; flex-direction: column; align-items: center;
    justify-content: center; gap: 56px;
  }
  .card {
    position: relative; width: 900px; height: 514px;
    border-radius: 34px; overflow: hidden;
  }
  .card-front { background: var(--card-green); }
  .card-back { background: var(--paper); }

  .front-wordmark {
    position: absolute; left: 0; right: 0; top: 50%;
    transform: translateY(-50%);
    text-align: center; color: var(--brand-green-deep);
    font-weight: 700; line-height: 1.15;
  }
  .front-wordmark .line-main { display: block; font-size: 64px; letter-spacing: 1px; }
  .front-wordmark .line-sub { display: block; font-size: 30px; letter-spacing: 2px; }

  .back-wordmark {
    position: absolute; left: 64px; top: 96px;
    color: var(--brand-green); font-weight: 700; line-height: 1.1;
  }
  .back-wordmark .line-main { display: block; font-size: 46px; }
  .back-wordmark .line-sub { display: block; font-size: 21px; letter-spacing: 1px; margin-top: 4px; }

  .address {
    position: absolute; right: 64px; top: 268px; text-align: right;
    font-size: 17px; color: var(--ink-soft); line-height: 1.4;
  }
  .person { position: absolute; left: 64px; top: 300px; }
  .person-name { font-size: 30px; font-weight: 700; color: var(--brand-green); }
  .person-title { font-size: 17px; color: var(--ink-soft); margin-top: 2px; }

  .rule { position: absolute; left: 64px; top: 362px; width: 780px; height: 14px; }

  .contact-list {
    position: absolute; left: 64px; top: 392px; list-style: none;
    font-size: 18px; color: var(--ink-soft);
  }
  .contact-list li { display: flex; align-items: center; gap: 14px; height: 32px; }
  .contact-list svg { width: 16px; height: 16px; fill: var(--brand-green); flex: none; }
</style>
</head>
<body>
<main class="stage">

  <section class="card card-front" aria-label="Card front">
    <div class="front-wordmark">
      <span class="line-main">The Manor</span>
      <span class="line-sub">at Brookridge Golf Club</span>
    </div>
  </section>

  <section class="card card-back" aria-label="Card back">
    <div class="back-wordmark">
      <span class="line-main">The Manor</span>
      <span class="line-sub">at Brookridge Golf Club</span>
    </div>

    <address class="address">2840 Alder Lane<br>Millbrook, MD 21090</address>

    <div class="person">
      <p class="person-name">Laura Whitfield</p>
      <p class="person-title">President - owner</p>
    </div>

    <svg class="rule" viewBox="0 0 780 14" aria-hidden="true">
      <line x1="0" y1="7" x2="766" y2="7" stroke="#cdbb98" stroke-width="2"/>
      <rect x="766" y="0" width="14" height="14" fill="#cdbb98"/>
    </svg>

    <ul class="contact-list">
      <li>
        <svg viewBox="0 0 16 16" aria-hidden="true"><path d="M3.6 1.2l2.3 2.5-1.2 1.6c.8 1.9 2.2 3.3 4.1 4.2l1.6-1.2 2.5 2.3-1.3 2.5C6.7 12.7 3.2 9.2 1.1 4.3z"/></svg>
        (410) 555-0148
      </li>
      <li>
        <svg viewBox="0 0 16 16" aria-hidden="true"><path d="M1 3h14v10H1z M1.8 3.8L8 8.6l6.2-4.8" fill="#6f8f24" stroke="#fdfdfb" stroke-width="1"/></svg>
        lwhitfield@brookridgegolfclub.com
      </li>
      <li>
        <svg viewBox="0 0 16 16" aria-hidden="true"><circle cx="8" cy="8" r="7"/><path d="M1 8h14M8 1c3 3 3 11 0 14M8 1c-3 3-3 11 0 14" fill="none" stroke="#fdfdfb" stroke-width="1"/></svg>
        www.brookridgegolfclub.com
      </li>
    </ul>
  </section>

</main>
</body>
</html>
```